Stationery Design needed for logo design project

This project is linked to Pediatric Therapy Clinic for children with autism and other special needs needs new logo design.

Our company needs a Stationery Design. Please refer to our original project in the link above.

Reason: Too much to do right now while enjoying Christmas with all my family!

```html
<!DOCTYPE html>
<html lang="en">
<head>
<meta charset="utf-8">
<title>Harbor Steps – Stationery Set</title>
<link href="https://fonts.googleapis.com/css2?family=Open+Sans:wght@400;600;700;800&family=Questrial&display=swap" rel="stylesheet">
<style>
:root{
  --red:#e84a27;
  --blue:#1aa7d0;
  --yellow:#fbb416;
  --green:#3fd41b;
  --ink:#333333;
  --paper:#ffffff;
  --field:#efefef;
  --backdrop:#e6e6e6;
}
*{box-sizing:border-box;margin:0;padding:0}
html,body{width:1200px;height:900px;overflow:hidden}
body{background:var(--backdrop);position:relative;font-family:'Open Sans',sans-serif;color:var(--ink)}
.sheet{position:absolute;background:var(--paper);box-shadow:0 2px 6px rgba(0,0,0,.15);overflow:hidden}

/* footer bands */
.bands{position:absolute;left:0;right:0;bottom:0}
.bands span{display:block}
.bands .band-red{background:var(--red)}
.bands .band-blue{background:var(--blue)}

/* brand block */
.brand{position:absolute;display:flex;flex-direction:column}
.brand-name{display:flex;align-items:center;gap:4px;font-family:'Open Sans',sans-serif;font-weight:800;color:var(--red);line-height:1}
.brand-dot{border-radius:50%;background:var(--green);flex:none}
.brand-service{font-weight:700;color:var(--red);line-height:1.1}
.brand-tagline{font-weight:600;color:var(--blue);line-height:1.1}

/* contact */
.contact{position:absolute;list-style:none;font-family:'Questrial',sans-serif;color:var(--ink)}
.contact li{display:flex;align-items:flex-start;gap:4px}
.contact svg{flex:none}

/* invoice */
.invoice{left:69px;top:66px;width:361px;height:466px}
.invoice-title{position:absolute;left:30px;top:80px;font-size:15px;font-weight:400}
.invoice-dates{position:absolute;left:30px;top:98px;font-size:6px;font-weight:700;line-height:1.3}
.party{position:absolute;top:122px;width:150px;height:67px;border:1px solid #dddddd;border-top:none}
.party-head{height:10px;font-size:6px;font-weight:700;color:#fff;padding-left:5px;line-height:10px}
.party.from{left:30px}.party.from .party-head{background:var(--red)}
.party.to{left:181px}.party.to .party-head{background:var(--blue)}
.party-logo{position:absolute;left:5px;top:18px;width:36px;height:32px;border:1px dashed #aaa;font-size:7px;display:flex;align-items:center;justify-content:center;color:#555}
.party-fields{position:absolute;left:45px;top:14px;right:3px;font-size:4.5px;line-height:1}
.party-fields span{display:block;background:var(--field);padding:1px 2px;margin-bottom:1px}
.items-label{position:absolute;left:32px;top:206px;font-size:6px;font-weight:700}
.items{position:absolute;left:30px;top:221px;width:300px;border-collapse:separate;border-spacing:0 4px;font-size:5.5px}
.items thead th{background:var(--yellow);color:#fff;font-weight:600;height:13px;text-align:left;padding:0 4px}
.items tbody td{background:var(--field);height:17px;padding:0 4px;border-right:2px solid #fff}
.items .qty{width:30px;text-align:center}
.items .price{width:40px}.items .total{width:48px}
.amount{position:absolute;left:248px;top:368px;width:81px;font-size:4.5px}
.amount-head{background:var(--green);color:#fff;font-weight:700;text-align:center;height:12px;line-height:12px;font-size:5.5px}
.amount-row{display:flex;height:12px;margin-top:2px}
.amount-row span{background:var(--field);padding-left:8px;line-height:12px;width:32px;margin-right:2px}
.amount-row i{background:var(--field);flex:1}

/* letterhead */
.letterhead{left:476px;top:66px;width:359px;height:466px}

/* envelope back */
.envelope-back{left:898px;top:66px;width:228px;height:480px}
.flap{position:absolute;right:0;top:0;width:64px;height:100%;background:var(--yellow);border-radius:30px 0 0 30px}
.flap-brand{position:absolute;left:50%;top:50%;transform:translate(-50%,-50%) rotate(90deg);color:#fff;text-align:center;white-space:nowrap}
.flap-brand b{display:block;font-weight:800;font-size:13px}
.flap-brand small{display:block;font-weight:700;font-size:5px}

/* business cards */
.card{width:250px;height:146px}
.card-back{left:40px;top:640px}
.card-front{left:305px;top:640px}
.card-values{position:absolute;left:22px;top:18px;font-family:'Questrial',sans-serif;font-size:9px;font-weight:700;line-height:1.2}
.card-values .v1{color:var(--red)}.card-values .v2{color:var(--yellow)}.card-values .v3{color:var(--green)}.card-values .v4{color:var(--blue)}

/* DL envelope */
.envelope{left:599px;top:594px;width:526px;height:249px}
.window{position:absolute;left:346px;top:110px;width:150px;height:68px;border-radius:8px;background:#f1f1f1;border:1px solid #e3e3e3}
</style>
</head>
<body>

<svg width="0" height="0" style="position:absolute" aria-hidden="true">
  <symbol id="i-home" viewBox="0 0 12 12"><path d="M6 1 0.5 6H2v5h3V8h2v3h3V6h1.5z" fill="#e84a27"/></symbol>
  <symbol id="i-phone" viewBox="0 0 12 12"><path d="M1 5c0-2 2-3 5-3s5 1 5 3l-2 .5-.5-1.5h-5L3 5.5zM2.5 6.5h7v4h-7z" fill="#1aa7d0"/><circle cx="6" cy="8.5" r="1.2" fill="#fff"/></symbol>
  <symbol id="i-mail" viewBox="0 0 12 12"><rect x=".5" y="2.5" width="11" height="7" fill="#fbb416"/><path d="M.5 2.5 6 6.5l5.5-4" fill="none" stroke="#fff" stroke-width=".8"/></symbol>
  <symbol id="i-web" viewBox="0 0 12 12"><circle cx="6" cy="6" r="5.3" fill="#3fd41b"/><path d="M.7 6h10.6M6 .7v10.6M2 3.3h8M2 8.7h8" stroke="#fff" stroke-width=".6" fill="none"/><ellipse cx="6" cy="6" rx="2.4" ry="5.3" fill="none" stroke="#fff" stroke-width=".6"/></symbol>
</svg>

<!-- Invoice -->
<section class="sheet invoice">
  <div class="brand" style="left:30px;top:22px">
    <span class="brand-name" style="font-size:15px"><i class="brand-dot" style="width:9px;height:9px"></i>Harbor Steps</span>
    <span class="brand-service" style="font-size:6.5px;margin-top:5px">Pediatric Therapy Services</span>
    <span class="brand-tagline" style="font-size:4.5px">Caring for kids - Supporting parents</span>
  </div>
  <ul class="contact" style="left:230px;top:24px;font-size:7px;line-height:1.5">
    <li><svg width="9" height="9"><use href="#i-home"/></svg>4410 Elm Row<br>Fairview, AR 72010</li>
    <li><svg width="9" height="9"><use href="#i-phone"/></svg>555-010-2480</li>
    <li><svg width="9" height="9"><use href="#i-mail"/></svg>hello@harborsteps.com</li>
    <li><svg width="9" height="9"><use href="#i-web"/></svg>harborsteps.com</li>
  </ul>
  <h1 class="invoice-title">Invoice</h1>
  <p class="invoice-dates">5 April, 2014<br>Payment due by 25 November 2014</p>

  <div class="party from">
    <div class="party-head">FROM</div>
    <div class="party-logo">LOGO</div>
    <div class="party-fields"><span>Your Address</span><span>Address Line 1</span><span>Town</span><span>Region/State</span><span>Zip/Postal Code</span></div>
  </div>
  <div class="party to">
    <div class="party-head">TO</div>
    <div class="party-logo">LOGO</div>
    <div class="party-fields"><span>Your Address</span><span>Address Line 1</span><span>Town</span><span>Region/State</span><span>Zip/Postal Code</span></div>
  </div>

  <p class="items-label">ITEMS</p>
  <table class="items">
    <thead><tr><th class="qty">Quantity</th><th>Description</th><th class="price">Unit Price</th><th class="total">Total</th></tr></thead>
    <tbody>
      <tr><td class="qty">2</td><td></td><td></td><td></td></tr>
      <tr><td class="qty">1</td><td></td><td></td><td></td></tr>
      <tr><td class="qty">3</td><td></td><td></td><td></td></tr>
      <tr><td class="qty">5</td><td></td><td></td><td></td></tr>
      <tr><td class="qty">4</td><td></td><td></td><td></td></tr>
      <tr><td class="qty">1</td><td></td><td></td><td></td></tr>
    </tbody>
  </table>

  <div class="amount">
    <div class="amount-head">AMOUNT DUE</div>
    <div class="amount-row"><span>SUBTOTAL</span><i></i></div>
    <div class="amount-row"><span>TAX</span><i></i></div>
    <div class="amount-row"><span>SHIPPING</span><i></i></div>
    <div class="amount-row"><span>TOTAL</span><i></i></div>
  </div>
</section>

<!-- Letterhead -->
<section class="sheet letterhead">
  <div class="brand" style="left:30px;top:48px">
    <span class="brand-name" style="font-size:17px"><i class="brand-dot" style="width:10px;height:10px"></i>Harbor Steps</span>
    <span class="brand-service" style="font-size:7.5px;margin-top:6px">Pediatric Therapy Services</span>
    <span class="brand-tagline" style="font-size:5.5px">Caring for kids - Supporting parents</span>
  </div>
  <ul class="contact" style="left:234px;top:40px;font-size:8px;line-height:1.5">
    <li><svg width="10" height="10"><use href="#i-home"/></svg>4410 Elm Row<br>Fairview, AR 72010</li>
    <li><svg width="10" height="10"><use href="#i-phone"/></svg>555-010-2480</li>
    <li><svg width="10" height="10"><use href="#i-mail"/></svg>hello@harborsteps.com</li>
    <li><svg width="10" height="10"><use href="#i-web"/></svg>harborsteps.com</li>
  </ul>
  <div class="bands" aria-hidden="true">
    <span class="band-red" style="height:8px;margin-bottom:4px"></span>
    <span class="band-blue" style="height:6px"></span>
  </div>
</section>

<!-- Envelope back -->
<section class="sheet envelope-back">
  <div class="flap">
    <div class="flap-brand"><b>Harbor Steps</b><small>Pediatric Therapy Services</small></div>
  </div>
</section>

<!-- Business card back -->
<section class="sheet card card-back">
  <p class="card-values">
    <span class="v1">CALM</span>, <span class="v2">KIND</span>, <span class="v3">PLAYFUL</span><br>
    <span class="v4">PATIENT</span>, <span class="v1">STEP BY STEP SPIRIT</span>
  </p>
  <ul class="contact" style="left:22px;top:50px;font-size:8px;line-height:1.5">
    <li><svg width="10" height="10"><use href="#i-home"/></svg>4410 Elm Row Fairview, AR 72010</li>
    <li><svg width="10" height="10"><use href="#i-phone"/></svg>555-010-2480</li>
    <li><svg width="10" height="10"><use href="#i-mail"/></svg>hello@harborsteps.com</li>
    <li><svg width="10" height="10"><use href="#i-web"/></svg>harborsteps.com</li>
  </ul>
  <div class="bands" aria-hidden="true">
    <span class="band-red" style="height:5px;margin-bottom:3px"></span>
    <span class="band-blue" style="height:4px"></span>
  </div>
</section>

<!-- Business card front -->
<section class="sheet card card-front">
  <div class="brand" style="left:0;right:0;top:42px;align-items:center;text-align:center">
    <span class="brand-name" style="font-size:20px"><i class="brand-dot" style="width:12px;height:12px"></i>Harbor Steps</span>
    <span class="brand-service" style="font-size:10px;margin-top:8px">Pediatric Therapy Services</span>
    <span class="brand-tagline" style="font-size:8px">Caring for kids - Supporting parents</span>
  </div>
</section>

<!-- DL envelope -->
<section class="sheet envelope">
  <div class="brand" style="left:30px;top:38px">
    <span class="brand-name" style="font-size:19px"><i class="brand-dot" style="width:12px;height:12px"></i>Harbor Steps</span>
    <span class="brand-service" style="font-size:8.5px;margin-top:8px">Pediatric Therapy Services</span>
    <span class="brand-tagline" style="font-size:6px">Caring for kids - Supporting parents</span>
  </div>
  <ul class="contact" style="left:360px;top:28px;font-size:11px;line-height:1.35">
    <li><svg width="14" height="14"><use href="#i-home"/></svg>4410 Elm Row<br>Fairview, AR 72010</li>
    <li><svg width="14" height="14"><use href="#i-phone"/></svg>555-010-2480</li>
    <li><svg width="14" height="14"><use href="#i-mail"/></svg>hello@harborsteps.com</li>
    <li><svg width="14" height="14"><use href="#i-web"/></svg>harborsteps.com</li>
  </ul>
  <div class="window"></div>
  <div class="bands" aria-hidden="true">
    <span class="band-red" style="height:8px;margin-bottom:5px"></span>
    <span class="band-blue" style="height:6px"></span>
  </div>
</section>

</body>
</html>
```